Business Card Design

We Import cars and commercial vehicles, we have been in business around 12 years, we are based in Christchurch, New Zealand.
I really like the web address on card, possibly right along the bottom of the card?
We specialize in commercial vans, maybe worth a mention?
The logo has the name in it so probably don't need to have twice?

I really like a clean smart look, not too cluttered

Industry/Entity Type

Business

Contact Information for Business Card

RQL TOKYO IMPORTS, Derek Holloway, Managing Director
web address: www.rqlmotorsnz.com
cell phone. 021 485 912

Requirements
Must have
• the logo, and all the contact details.

Forgot to add my email address, derek@rqlmotorsnz.com
Nice to have
• Just thinking as the card is looking a little empty maybe somewhere written what we do? 'Specializing in commercial vans'
Not sure but we import Japanese vehicles, possibly adding some brands like Velkara Poremo Ketsu Brivon etc? Not sure on that one.

```html
<!DOCTYPE html>
<html lang="en">
<head>
<meta charset="UTF-8">
<title>RQL Tokyo Imports – Business Card</title>
<link rel="stylesheet" href="https://fonts.googleapis.com/css2?family=Exo+2:wght@500;600&display=swap">
<style>
  :root {
    --band-grey: #bdbdbd;
    --card-black: #000000;
    --ink: #141414;
    --stripe-dark: #6b6b6b;
    --stripe-white: #ffffff;
    --name-white: #ffffff;
    --contact-grey: #b5b5b5;
    --van-light: #e6e6e6;
    --van-dark: #7a7a7a;
  }
  * { margin: 0; padding: 0; box-sizing: border-box; }
  html, body {
    width: 1200px; height: 726px; overflow: hidden;
    background: var(--card-black);
    font-family: "Exo 2", sans-serif;
  }
  .card {
    position: relative; width: 1200px; height: 726px;
    background: var(--card-black); overflow: hidden;
  }
  .top-band {
    position: absolute; left: 0; top: 0; width: 1200px; height: 340px;
    background: var(--band-grey);
  }
  .band-stripes { position: absolute; left: 0; top: 0; }
  .brand-name {
    position: absolute; left: 88px; top: 110px;
    font-weight: 600; font-size: 50px; line-height: 1.2;
    color: var(--ink); white-space: nowrap;
  }
  .van-illustration {
    position: absolute; left: 556px; top: 50px; width: 260px; height: 174px;
    border-radius: 40px 60px 24px 24px;
    background: linear-gradient(180deg, var(--van-light) 0%, var(--van-light) 55%, var(--van-dark) 100%);
  }
  .tagline {
    position: absolute; left: 86px; top: 264px;
    font-weight: 600; font-size: 34px; color: var(--ink); white-space: nowrap;
  }
  .person {
    position: absolute; left: 270px; top: 468px; transform: translateX(-50%);
    text-align: center; color: var(--name-white); white-space: nowrap;
  }
  .person-name { font-weight: 500; font-size: 44px; line-height: 1.2; }
  .person-title { font-weight: 500; font-size: 26px; margin-top: 8px; }
  .contact-list {
    position: absolute; left: 636px; top: 440px; list-style: none;
    color: var(--contact-grey); font-weight: 500; font-size: 35px;
  }
  .contact-item { display: flex; align-items: center; height: 56px; white-space: nowrap; }
  .contact-icon { width: 30px; height: 30px; margin-right: 22px; flex: none; }
</style>
</head>
<body>
<div class="card">
  <div class="top-band"></div>
  <svg class="band-stripes" width="1200" height="340" viewBox="0 0 1200 340">
    <polygon points="1060,0 1115,0 900,340 845,340" fill="var(--card-black)"/>
    <polygon points="1125,0 1140,0 925,340 910,340" fill="var(--stripe-white)"/>
    <polygon points="1150,0 1200,0 1200,30 1005,340 935,340" fill="var(--card-black)"/>
    <polygon points="1200,60 1200,340 1023,340" fill="var(--stripe-dark)"/>
  </svg>

  <div class="brand-name">RQL Tokyo Imports</div>
  <div class="van-illustration" role="img" aria-label="Illustration of a white commercial van"></div>
  <p class="tagline">We specialize in commercial vans</p>

  <div class="person">
    <div class="person-name">Derek Holloway</div>
    <div class="person-title">Managing Director</div>
  </div>

  <ul class="contact-list">
    <li class="contact-item">
      <svg class="contact-icon" viewBox="0 0 24 24" aria-hidden="true"><path fill="currentColor" d="M6.6 10.8a15.1 15.1 0 0 0 6.6 6.6l2.2-2.2c.3-.3.7-.4 1-.2 1.1.4 2.3.6 3.6.6.6 0 1 .4 1 1V20c0 .6-.4 1-1 1A17 17 0 0 1 3 4c0-.6.4-1 1-1h3.5c.6 0 1 .4 1 1 0 1.3.2 2.5.6 3.6.1.3 0 .7-.2 1z"/></svg>
      <span>021 485 912</span>
    </li>
    <li class="contact-item">
      <svg class="contact-icon" viewBox="0 0 24 24" aria-hidden="true"><path fill="currentColor" d="M3 6h18v12H3z"/><path d="M3 6l9 7 9-7" fill="none" stroke="var(--card-black)" stroke-width="1.8"/></svg>
      <span>derek@rqlmotorsnz.com</span>
    </li>
    <li class="contact-item">
      <svg class="contact-icon" viewBox="0 0 24 24" aria-hidden="true"><circle cx="12" cy="12" r="10" fill="currentColor"/><path d="M2 12h20M12 2c3 3 3 17 0 20M12 2c-3 3-3 17 0 20" fill="none" stroke="var(--card-black)" stroke-width="1.6"/></svg>
      <span>www.rqlmotorsnz.com</span>
    </li>
  </ul>
</div>
</body>
</html>
```